Brintell's Business Card

I need some designs for a new business card including the new logo attached. An old example of our business card is also attached to show all the data that should be included on the new design.
**I added some more examples someone had mocked up**

Contact Information for Business Card

Should include all info on other examples uploaded.

```html
<!DOCTYPE html>
<html lang="en">
<head>
<meta charset="utf-8">
<title>Brintell's Business Card</title>
<link href="https://fonts.googleapis.com/css2?family=Montserrat:wght@400;600;700&display=swap" rel="stylesheet">
<style>
  :root{
    --backdrop:#ababab;
    --card-white:#ffffff;
    --brand-blue:#0a6cb4;
    --brand-red:#e5262f;
    --text-gray:#6f6f6f;
    --gradient-red:#c0304a;
    --gradient-mid:#5a5a90;
    --gradient-blue:#0070bd;
  }
  html,body{margin:0;padding:0;width:1200px;height:1000px;overflow:hidden;background:var(--backdrop);}
  body{position:relative;font-family:'Montserrat',sans-serif;}
  .card{position:absolute;left:294px;width:613px;height:352px;border-radius:26px;overflow:hidden;}
  .card-front{top:94px;background:var(--card-white);}
  .card-back{top:530px;background:linear-gradient(90deg,var(--gradient-red) 0%,var(--gradient-mid) 38%,var(--gradient-blue) 62%,var(--gradient-blue) 100%);}
  .brand-name{position:absolute;margin:0;font-weight:700;font-size:28px;letter-spacing:.5px;line-height:1;}
  .card-front .brand-name{left:60px;top:58px;color:var(--brand-blue);}
  .card-back .brand-name{right:48px;top:261px;color:#fff;}
  .person-name{position:absolute;left:60px;top:142px;margin:0;font-weight:600;font-size:22px;color:var(--brand-blue);}
  .address{position:absolute;left:59px;top:185px;margin:0;font-size:17px;line-height:21px;color:var(--text-gray);font-style:normal;letter-spacing:.3px;}
  .contact{position:absolute;left:59px;top:250px;margin:0;padding:0;list-style:none;font-size:17px;line-height:21px;color:var(--text-gray);letter-spacing:.3px;}
  .contact li{display:flex;align-items:center;gap:5px;}
  .contact svg{width:12px;height:12px;fill:var(--brand-red);}
  .badge{position:absolute;left:393px;top:141px;width:190px;height:190px;}
  .back-decoration{position:absolute;left:0;top:0;width:260px;height:352px;}
</style>
</head>
<body>
  <section class="card card-front">
    <p class="brand-name">BRINTELL'S</p>
    <h1 class="person-name">Dylan Brintell</h1>
    <address class="address">418 Maple Ridge Road<br>Oakhaven, IA 50999, EUA</address>
    <ul class="contact">
      <li><svg viewBox="0 0 24 24" aria-hidden="true"><path d="M6.6 10.8c1.4 2.8 3.8 5.1 6.6 6.6l2.2-2.2c.3-.3.7-.4 1-.2 1.1.4 2.3.6 3.6.6.6 0 1 .4 1 1V20c0 .6-.4 1-1 1C10.6 21 3 13.4 3 4c0-.6.4-1 1-1h3.5c.6 0 1 .4 1 1 0 1.3.2 2.5.6 3.6.1.3 0 .7-.2 1z"/></svg>555.014.2278</li>
      <li><svg viewBox="0 0 24 24" aria-hidden="true"><path d="M2 5h20v14H2z M2 5l10 8 10-8" /></svg>hvacbrintell@mailbox.com</li>
    </ul>
    <svg class="badge" viewBox="0 0 190 190" aria-hidden="true">
      <circle cx="95" cy="95" r="90" fill="none" stroke="var(--brand-blue)" stroke-width="3"/>
      <circle cx="95" cy="95" r="62" fill="none" stroke="var(--brand-red)" stroke-width="3"/>
    </svg>
  </section>

  <section class="card card-back">
    <div class="back-decoration" role="img" aria-label="Faint large brand emblem decoration"></div>
    <p class="brand-name">BRINTELL'S</p>
  </section>
</body>
</html>
```